Criação de Papelaria Profissional para Limpeza & Serviço para o lar
A empresa queria:
" Terceirizamos serviços de limpeza empresarial, portaria, recepção, copeira, limpeza pós-obra "

```html
<!DOCTYPE html>
<html lang="pt-BR">
<head>
<meta charset="utf-8">
<title>BomLar – Papel Timbrado</title>
<link rel="stylesheet" href="https://fonts.googleapis.com/css2?family=Roboto:wght@300;400;500;700&display=swap">
<style>
  :root {
    --bg: #e9e9e7;
    --paper: #ffffff;
    --ink: #1c1c1c;
    --ink-soft: #555555;
    --green: #6bb43f;
    --blue: #1d5fa8;
    --blue-light: #4f8fd0;
  }
  * { box-sizing: border-box; margin: 0; padding: 0; }
  html, body {
    width: 1200px; height: 1200px; overflow: hidden;
    background: var(--bg);
    font-family: "Roboto", Arial, sans-serif;
    color: var(--ink);
  }
  .letterhead {
    position: absolute;
    left: 200px; top: 24px;
    width: 800px; height: 1152px;
    background: var(--paper);
    box-shadow: 0 2px 10px rgba(0,0,0,.12);
    overflow: hidden;
  }
  .brand {
    position: absolute; right: 74px; top: 150px;
    display: flex; align-items: center; gap: 12px;
  }
  .brand-mark {
    width: 26px; height: 26px; border-radius: 50%;
    background: var(--green);
  }
  .brand-name {
    font-size: 40px; font-weight: 700; color: var(--blue);
    letter-spacing: -.5px;
  }
  .title {
    position: absolute; left: 74px; top: 262px;
    font-size: 36px; font-weight: 400; letter-spacing: .5px;
  }
  .body-text {
    position: absolute; left: 74px; right: 74px; top: 326px;
    font-size: 12.4px; line-height: 1.62; color: #2a2a2a;
    text-align: justify;
  }
  .body-text p { margin-bottom: 26px; }
  .signature {
    position: absolute; left: 50%; top: 920px;
    transform: translateX(-40%);
    text-align: right;
  }
  .signature-scribble {
    width: 220px; height: 70px;
    background: linear-gradient(90deg, rgba(0,0,0,0), rgba(0,0,0,.12), rgba(0,0,0,0));
    border-radius: 6px;
  }
  .signature-name { font-size: 12px; font-weight: 700; margin-top: 2px; }
  .signature-role { font-size: 11px; color: var(--green); }
  .contacts {
    position: absolute; left: 74px; right: 40px; top: 1090px;
    display: flex; justify-content: space-between; align-items: center;
  }
  .contact { display: flex; align-items: center; gap: 8px; }
  .contact-icon {
    width: 20px; height: 20px; border-radius: 50%;
    background: var(--green);
    display: flex; align-items: center; justify-content: center;
  }
  .contact-text {
    font-size: 8.5px; line-height: 1.35; color: var(--ink-soft);
    text-transform: uppercase;
  }
  .footer-band {
    position: absolute; left: 0; right: 0; bottom: 0; height: 18px;
    background: linear-gradient(90deg, var(--blue-light), var(--blue) 60%, var(--blue-light));
  }
</style>
</head>
<body>
  <main class="letterhead">
    <header class="brand">
      <span class="brand-mark"></span>
      <span class="brand-name">BomLar</span>
    </header>

    <h1 class="title">TÍTULO</h1>

    <section class="body-text">
      <p>Lorem Ipsum é simplesmente uma simulação de texto da indústria tipográfica e de impressos, e vem sendo utilizado desde o século XVI, quando um impressor desconhecido pegou uma bandeja de tipos e os embaralhou para fazer um livro de modelos de tipos. Lorem Ipsum sobreviveu não só a cinco séculos, como também ao salto para a editoração eletrônica, permanecendo essencialmente inalterado. Se popularizou na década de 60, quando uma gráfica lançou decalques contendo passagens de Lorem Ipsum, e mais recentemente quando passou a ser integrado a programas de diagramação e editoração eletrônica.</p>
      <p>Lorem Ipsum é simplesmente uma simulação de texto da indústria tipográfica e de impressos, e vem sendo utilizado desde o século XVI, quando um impressor desconhecido pegou uma bandeja de tipos e os embaralhou para fazer um livro de modelos de tipos. Lorem Ipsum sobreviveu não só a cinco séculos, como também ao salto para a editoração eletrônica, permanecendo essencialmente inalterado. Se popularizou na década de 60, quan</p>
      <p>Lorem Ipsum é simplesmente uma simulação de texto da indústria tipográfica e de impressos, e vem sendo utilizado desde o século XVI, quando um impressor desconhecido pegou uma bandeja de tipos e os embaralhou para fazer</p>
      <p>Lorem Ipsum é simplesmente uma simulação de texto da indústria tipográfica e de impressos, e vem sendo utilizado desde o século XVI, quando um impressor desconhecido pegou uma bandeja de tipos e os embaralhou para fazer</p>
      <p>Lorem Ipsum é simplesmente uma simulação de texto da indústria tipográfica e de impressos, e vem sendo utilizado desde o século XVI, quando um impressor desconhecido pegou uma bandeja de tipos e os embaralhou para fazer</p>
      <p>Lorem Ipsum é simplesmente uma simulação de texto da indústria tipográfica e de impressos, e vem sendo utilizado desde o século XVI, quando um impressor desconhecido pegou uma bandeja de tipos e os embaralhou para fazer</p>
    </section>

    <div class="signature">
      <div class="signature-scribble" role="img" aria-label="Assinatura manuscrita do responsável"></div>
      <div class="signature-name">Nome do Responsável</div>
      <div class="signature-role">Cargo</div>
    </div>

    <footer class="contacts">
      <div class="contact">
        <span class="contact-icon">
          <svg width="11" height="11" viewBox="0 0 24 24" fill="#fff"><path d="M6.6 10.8a15.1 15.1 0 0 0 6.6 6.6l2.2-2.2c.3-.3.7-.4 1-.2 1.1.4 2.3.6 3.6.6.6 0 1 .4 1 1V20c0 .6-.4 1-1 1A17 17 0 0 1 3 4c0-.6.4-1 1-1h3.5c.6 0 1 .4 1 1 0 1.3.2 2.5.6 3.6.1.3 0 .7-.2 1z"/></svg>
        </span>
        <span class="contact-text">00 0000 0000<br>00 0000 0000</span>
      </div>
      <div class="contact">
        <span class="contact-icon">
          <svg width="11" height="11" viewBox="0 0 24 24"><path d="M3 5h18v14H3z" fill="none" stroke="#fff" stroke-width="2"/><path d="M3 6l9 7 9-7" fill="none" stroke="#fff" stroke-width="2"/></svg>
        </span>
        <span class="contact-text">contato@bomlar.com.br<br>contato@bomlar.com.br</span>
      </div>
      <div class="contact">
        <span class="contact-icon">
          <svg width="11" height="11" viewBox="0 0 24 24" fill="none" stroke="#fff" stroke-width="2"><circle cx="12" cy="12" r="9"/><path d="M3 12h18M12 3c3 3 3 15 0 18M12 3c-3 3-3 15 0 18"/></svg>
        </span>
        <span class="contact-text">www.bomlar.com.br<br>contato@bomlar.com.br</span>
      </div>
      <div class="contact">
        <span class="contact-icon">
          <svg width="11" height="11" viewBox="0 0 24 24" fill="#fff"><path d="M12 2a7 7 0 0 0-7 7c0 5 7 13 7 13s7-8 7-13a7 7 0 0 0-7-7zm0 9.5a2.5 2.5 0 1 1 0-5 2.5 2.5 0 0 1 0 5z"/></svg>
        </span>
        <span class="contact-text">Nome da Rua, 000 - Bairro<br>Cidade - Estado - CEP 0000</span>
      </div>
    </footer>

    <div class="footer-band"></div>
  </main>
</body>
</html>
```